Construction company that specializes in roofing and siding

https://havenridgeroofs.example/featured-projects/

https://www.pinecrestrenovationllc.example/#

https://www.ironmeadowhomes.example/residential-siding-services/

Please model a website after these examples
I posted a doc that has some content to get you started. I will upload more content and photos as the site progresses.

Coded - Design and coding required

5+ page

```html
<!DOCTYPE html>
<html lang="en">
<head>
<meta charset="utf-8">
<title>Stoneward Construction — Roofing &amp; Siding in Minnesota</title>
<link rel="stylesheet" href="https://fonts.googleapis.com/css2?family=Poppins:ital,wght@0,400;0,500;0,600;0,700;1,500&family=Jost:wght@300;400;500&display=swap">
<style>
:root{
  --ink:#1f1d4a;
  --muted:#8c8c8c;
  --dark:#232323;
  --black:#111111;
  --panel:#dcdcdc;
  --field:#e3e3e3;
  --white:#ffffff;
  --body:#6e6e6e;
  --star:#f08a1c;
}
*{box-sizing:border-box;margin:0;padding:0}
html,body{width:1200px;height:4788px;overflow:hidden;background:var(--white)}
body{position:relative;font-family:"Jost",sans-serif;color:var(--ink)}
.abs{position:absolute}
h1,h2,h3,.caps{font-family:"Poppins",sans-serif}

/* header */
.site-header{position:absolute;left:0;top:0;width:1200px;height:115px;background:var(--black)}
.brand{position:absolute;left:0;top:0;width:244px;height:115px;background:var(--white);display:flex;align-items:center;gap:12px;padding-left:30px}
.brand-mark{width:40px;height:40px;border-radius:50%;background:var(--dark)}
.brand-name{font-family:"Poppins",sans-serif;font-weight:600;font-size:17px;color:var(--dark);letter-spacing:1px;line-height:1.1}
.topbar{position:absolute;left:298px;top:16px;width:840px;font-size:9px;color:#cfcfcf;display:flex;justify-content:space-between}
.topbar .contacts{display:flex;gap:24px}
.topbar svg{vertical-align:-2px;margin-right:5px}
.main-nav{position:absolute;left:298px;top:64px;display:flex;gap:0;font-family:"Poppins",sans-serif;font-size:13px;font-weight:500;color:var(--white)}
.main-nav a{color:inherit;text-decoration:none;margin-right:58px}
.nav-cta{position:absolute;left:1036px;top:60px;width:112px;height:22px;background:#9a9a9a;color:var(--white);font-size:8px;font-family:"Poppins",sans-serif;display:flex;align-items:center;justify-content:center}

/* hero */
.hero{position:absolute;left:0;top:115px;width:1200px;height:717px;background:linear-gradient(180deg,#56606d 0%,#39404a 35%,#22262c 75%,#1a1c20 100%)}
.hero-kicker{position:absolute;left:64px;top:210px;font-family:"Poppins",sans-serif;font-size:20px;color:var(--white)}
.hero-title{position:absolute;left:60px;top:262px;font-size:34px;line-height:44px;font-weight:700;color:var(--white)}
.btn-dark{background:var(--black);color:var(--white);font-family:"Poppins",sans-serif;font-weight:500;display:flex;align-items:center;justify-content:center;text-decoration:none}
.hero-btn{position:absolute;left:63px;top:381px;width:192px;height:39px;font-size:15px}

.quote-form{position:absolute;left:682px;top:188px;width:390px;height:479px;background:var(--white)}
.quote-form h2{position:absolute;left:0;right:0;top:48px;text-align:center;font-size:27px;font-weight:600;color:var(--black)}
.field{position:absolute;background:var(--field);font-size:10px;color:#6a6a6a;padding:13px 20px;text-transform:uppercase}
.field.sel{text-transform:none}
.quote-form .submit{position:absolute;left:106px;top:402px;width:192px;height:40px;font-size:15px}

/* services */
.service{position:absolute;top:725px;width:285px;height:330px;filter:drop-shadow(0 6px 14px rgba(0,0,0,.12))}
.service .shape{position:absolute;inset:0;background:var(--white);clip-path:polygon(0 107px,50% 0,100% 107px,100% 100%,0 100%)}
.service .icon{position:absolute;left:71px;top:3px;width:143px;height:112px;background:var(--black);display:flex;align-items:center;justify-content:center}
.service h3{position:absolute;top:162px;width:100%;text-align:center;font-size:25px;font-weight:600;color:var(--ink)}
.service p{position:absolute;top:208px;left:28px;right:28px;text-align:center;font-size:12.5px;line-height:16px;color:var(--body)}
.service .btn-dark{position:absolute;left:62px;top:278px;width:161px;height:37px;font-size:15px}

.dots{position:absolute;display:flex;gap:15px}
.dots span{width:18px;height:18px;border-radius:50%;background:#b3b3b3}
.dots span.on{background:var(--black)}

/* headings */
.section-title{position:absolute;font-size:34px;font-weight:600;color:var(--ink)}
.section-title span{color:var(--muted)}
.section-title.light{color:var(--white)}

/* about */
.about-copy{position:absolute;left:130px;top:1314px;width:490px;font-size:15px;line-height:22px;color:var(--body)}
.stat{position:absolute;top:1462px;width:120px}
.stat p{font-family:"Poppins",sans-serif;font-size:13px;font-weight:500;line-height:16px;color:var(--ink);margin-top:14px}

/* work */
.work{position:absolute;left:0;top:1752px;width:1200px;height:976px;background:var(--dark)}
.tabs{position:absolute;left:136px;top:199px;display:flex;gap:19px}
.tabs span{width:168px;height:51px;background:var(--panel);display:flex;align-items:center;justify-content:center;font-family:"Poppins",sans-serif;font-size:18px;font-weight:500;color:var(--ink)}
.photo{position:absolute;width:286px;height:231px}
.work .explore{position:absolute;left:509px;top:877px;width:191px;height:38px;background:var(--panel);font-family:"Poppins",sans-serif;font-weight:600;font-size:15px;color:var(--ink);display:flex;align-items:center;justify-content:center}

/* why */
.feature{position:absolute;width:234px;height:106px;background:var(--white);border:1px solid #e2e2e2;box-shadow:0 4px 12px rgba(0,0,0,.12);padding:20px 12px 0 86px}
.feature svg{position:absolute;left:18px;top:26px}
.feature h3{font-size:17px;font-weight:500;color:var(--black);margin-bottom:4px}
.feature p{font-size:9.5px;line-height:13px;color:#8a8a8a}

/* owner quote */
.promise{position:absolute;left:0;top:3458px;width:1200px;height:249px;background:linear-gradient(180deg,#2c2c2e,#3a3a3c 60%,#2a2a2b)}
.promise blockquote{position:absolute;left:141px;top:97px;width:620px;font-family:"Poppins",sans-serif;font-style:italic;font-weight:500;font-size:17px;line-height:24px;color:var(--white)}
.promise .rule{position:absolute;left:812px;top:83px;width:2px;height:80px;background:#bdbdbd}
.promise .owner{position:absolute;left:858px;top:104px;font-family:"Poppins",sans-serif;font-size:17px;font-weight:500;color:var(--white)}
.promise .role{position:absolute;left:862px;top:130px;font-size:15px;color:#8d8d8d}

/* testimonials */
.review{position:absolute;top:3939px;width:287px;height:223px;background:var(--white);border:1px solid #e6e6e6;box-shadow:0 4px 14px rgba(0,0,0,.12)}
.review .avatar{position:absolute;left:22px;top:52px;width:42px;height:42px;border-radius:50%;background:linear-gradient(180deg,#9fb2c4 0%,#6f8a58 60%,#3f5335 100%)}
.review .who{position:absolute;left:76px;top:54px;font-family:"Poppins",sans-serif;font-size:10px;font-weight:600;color:var(--black)}
.review .stars{position:absolute;left:76px;top:70px;font-size:12px;letter-spacing:2px;color:var(--star)}
.review p{position:absolute;left:20px;top:110px;width:240px;font-size:10.5px;line-height:16px;color:#8c8c8c}

/* footer */
.site-footer{position:absolute;left:0;top:4309px;width:1200px;height:479px;background:var(--dark);color:var(--white);text-align:center}
.footer-brand{position:absolute;left:0;right:0;top:76px;display:flex;justify-content:center;align-items:center;gap:16px}
.footer-brand .brand-mark{background:#7a7a7a;width:52px;height:52px}
.footer-brand .brand-name{color:#9a9a9a;font-size:22px}
.footer-tag{position:absolute;left:0;right:0;top:160px;font-size:17px;line-height:22px}
.footer-links{position:absolute;left:0;right:0;top:225px;font-size:20px}
.footer-contact{position:absolute;left:218px;top:292px;display:flex;gap:48px;font-size:17px;align-items:center}
.footer-contact span{display:flex;align-items:center;gap:14px}
.copyright{position:absolute;left:0;right:0;top:398px;font-size:15px}
</style>
</head>
<body>

<header class="site-header">
  <div class="brand"><span class="brand-mark"></span><span class="brand-name">STONEWARD<br>CONSTRUCTION</span></div>
  <div class="topbar">
    <span>Welcome to Stoneward Construction</span>
    <span class="contacts">
      <span><svg width="10" height="10" viewBox="0 0 24 24"><path fill="#fff" d="M6.6 10.8a15 15 0 006.6 6.6l2.2-2.2c.3-.3.7-.4 1-.2 1.1.4 2.3.6 3.6.6.6 0 1 .4 1 1V20c0 .6-.4 1-1 1A17 17 0 013 4c0-.6.4-1 1-1h3.5c.6 0 1 .4 1 1 0 1.3.2 2.5.6 3.6.1.3 0 .7-.2 1z"/></svg>(+1) 555 014 2290</span>
      <span><svg width="11" height="10" viewBox="0 0 24 20"><path fill="#fff" d="M2 2h20v16H2zM3 3l9 7 9-7"/></svg>hello@stonewardbuild.example</span>
    </span>
  </div>
  <nav class="main-nav">
    <a href="#">ROOFING</a><a href="#">SIDING</a><a href="#">GUTTERS</a><a href="#">WINDOWS</a><a href="#">REPAIR</a><a href="#">DAMAGE REPAIR</a>
  </nav>
  <a class="nav-cta">GET A QUOTE</a>
</header>

<section class="hero" role="img" aria-label="Photo of a dark tiled roof under an overcast sky">
  <p class="hero-kicker">ROOFING | SIDING | WINDOWS | GUTTERS</p>
  <h1 class="hero-title">YOUR SOURCE FOR ROOFING<br>AND SIDING IN MINNESOTA</h1>
  <a class="btn-dark hero-btn">OUR SERVICES</a>
</section>

<form class="quote-form">
  <h2>GET A QUOTE</h2>
  <div class="field" style="left:40px;top:122px;width:147px;height:38px">Name</div>
  <div class="field" style="left:204px;top:122px;width:147px;height:38px">Email</div>
  <div class="field" style="left:40px;top:173px;width:147px;height:38px">Phone</div>
  <div class="field" style="left:204px;top:173px;width:147px;height:38px">Address</div>
  <div class="field sel" style="left:42px;top:224px;width:311px;height:38px">Select Service</div>
  <div class="field" style="left:40px;top:277px;width:312px;height:88px">Additional Message</div>
  <a class="btn-dark submit">GET A QUOTE</a>
</form>

<article class="service" style="left:119px">
  <div class="shape"></div>
  <div class="icon"><svg width="76" height="64" viewBox="0 0 76 64" fill="none" stroke="#fff" stroke-width="2.5"><path d="M6 58L20 24h50L56 58z"/><path d="M20 24V8h10v16M13 41h50M33 24l-8 34M48 24l-6 34"/></svg></div>
  <h3>ROOFING</h3>
  <p>Lorem ipsum dolor sit amet, consetetur sadipscing elitr, sed diam nonumy eirmod tempor invidunt ut labore</p>
  <a class="btn-dark">READ MORE</a>
</article>
<article class="service" style="left:451px">
  <div class="shape"></div>
  <div class="icon"><svg width="70" height="70" viewBox="0 0 70 70" fill="none" stroke="#fff" stroke-width="2.5"><path d="M5 34L35 6l30 28M13 27v38h44V27"/><path d="M23 36h24v22H23zM35 36v22M23 47h24"/></svg></div>
  <h3>SIDING</h3>
  <p>Lorem ipsum dolor sit amet, consetetur sadipscing elitr, sed diam nonumy eirmod tempor invidunt ut labore</p>
  <a class="btn-dark">READ MORE</a>
</article>
<article class="service" style="left:786px">
  <div class="shape"></div>
  <div class="icon"><svg width="66" height="66" viewBox="0 0 66 66" fill="none" stroke="#fff" stroke-width="2.5"><rect x="5" y="5" width="56" height="56"/><rect x="11" y="11" width="44" height="44"/><path d="M33 11v44M11 33h44M38 50l12-12M16 28l12-12"/></svg></div>
  <h3>WINDOWS</h3>
  <p>Lorem ipsum dolor sit amet, consetetur sadipscing elitr, sed diam nonumy eirmod tempor invidunt ut labore</p>
  <a class="btn-dark">READ MORE</a>
</article>
<div class="dots" style="left:553px;top:1102px"><span></span><span class="on"></span><span></span></div>

<!-- About -->
<h2 class="section-title" style="left:130px;top:1238px">ABOUT <span>US</span></h2>
<p class="about-copy">In 2016 Dale Harmon started helping people with their home improvement projects. His very first job was installing window trim for a wonderful homeowner in Forest lake MN.He did his best work and made sure he treated his first customer like family. Afterall, his first customer was Rosa Harmon, his Mom.</p>
<div class="stat" style="left:132px">
  <svg width="72" height="70" viewBox="0 0 72 70" fill="none" stroke="#1c1c1c" stroke-width="2.4"><circle cx="34" cy="36" r="14"/><path d="M18 36a16 16 0 0132 0M14 66c2-10 10-16 20-16s18 6 20 16"/><rect x="44" y="4" width="24" height="16" rx="3"/><path d="M50 12h12"/></svg>
  <p>Emergency<br>Response</p>
</div>
<div class="stat" style="left:306px">
  <svg width="72" height="70" viewBox="0 0 72 70" fill="none" stroke="#1c1c1c" stroke-width="2.4"><path d="M18 8C6 24 8 50 36 64C64 50 66 24 54 8"/><path d="M14 20l-6-4M10 32l-7-1M12 44l-6 3M58 20l6-4M62 32l7-1M60 44l6 3"/></svg>
  <p>20+ Years<br>in Business</p>
</div>
<div class="stat" style="left:480px">
  <svg width="72" height="70" viewBox="0 0 72 70" fill="none" stroke="#1c1c1c" stroke-width="2.4"><rect x="10" y="4" width="56" height="22" rx="2"/><path d="M20 15l2-4 2 4h-4M36 15l2-4 2 4h-4M52 15l2-4 2 4h-4"/><path d="M14 64V40c0-4 8-4 8 0v-12c0-4 8-4 8 0v14h14c6 0 6 8 0 8H34v14z"/></svg>
  <p>5k+ Satisfies<br>Clients</p>
</div>
<svg class="abs" style="left:660px;top:1221px" width="427" height="414" viewBox="0 0 427 414" role="img" aria-label="Shield-framed photo of a roofer in a hard hat cutting a metal roof panel">
  <defs><linearGradient id="aboutPhoto" x1="0" y1="0" x2="0" y2="1"><stop offset="0" stop-color="#a9c6e4"/><stop offset=".55" stop-color="#d8d1c6"/><stop offset="1" stop-color="#5a5d63"/></linearGradient></defs>
  <path d="M213 0L427 56c0 170-60 290-214 358C59 346 0 226 0 56z" fill="#6f6f6f"/>
  <path d="M213 36L391 74c-4 148-58 240-178 296C93 314 39 222 35 74z" fill="url(#aboutPhoto)"/>
</svg>

<!-- Work -->
<section class="work">
  <h2 class="section-title light" style="left:0;right:0;top:108px;text-align:center">OUR AWESOME <span>WORK</span></h2>
  <div class="tabs"><span>ROOFING</span><span>SIDING</span><span>GUTTERS</span><span>WINDOWS</span><span>ALL WORK</span></div>
  <div class="photo" style="left:141px;top:314px;background:linear-gradient(135deg,#8a8c92,#4a4c52 55%,#2f3034)" role="img" aria-label="Roofer fastening dark metal roof panels"></div>
  <div class="photo" style="left:455px;top:314px;background:linear-gradient(180deg,#b9d0e6,#d7d2cb 55%,#4b4d52)" role="img" aria-label="Worker in hard hat cutting roof sheeting"></div>
  <div class="photo" style="left:767px;top:314px;background:linear-gradient(135deg,#c98a48,#8d5a2e 50%,#6d7a3a)" role="img" aria-label="Carpenter in safety vest working on timber roof frame"></div>
  <div class="photo" style="left:141px;top:574px;background:linear-gradient(135deg,#d39653,#a46a34 50%,#5f6b3a)" role="img" aria-label="Builder measuring wooden rafters"></div>
  <div class="photo" style="left:455px;top:574px;background:linear-gradient(180deg,#7f9bb8,#a6a29c 50%,#6b6660)" role="img" aria-label="Roofers laying shingles on a pitched roof"></div>
  <div class="photo" style="left:767px;top:574px;background:linear-gradient(180deg,#e4e4e4,#9b5a3e 45%,#7a4430 80%,#c8a060)" role="img" aria-label="House with brown clay tile roof"></div>
  <a class="explore">EXPLORE MORE</a>
</section>

<!-- Why choose us -->
<h2 class="section-title" style="left:0;right:0;top:2856px;text-align:center">WHY CHOOSE <span>US</span></h2>
<svg class="abs" style="left:431px;top:3019px" width="346" height="340" viewBox="0 0 346 340" role="img" aria-label="Shield-framed photo of a two-storey house with a shingled gable roof">
  <defs><linearGradient id="whyPhoto" x1="0" y1="0" x2="0" y2="1"><stop offset="0" stop-color="#3f7fd0"/><stop offset=".45" stop-color="#9a8f7a"/><stop offset=".8" stop-color="#7b8a48"/><stop offset="1" stop-color="#566b35"/></linearGradient></defs>
  <path d="M173 0L346 40c-2 140-52 240-173 300C52 280 2 180 0 40z" fill="#6c6c6c"/>
  <path d="M173 30L318 62c-4 118-46 198-145 250C74 260 32 180 28 62z" fill="url(#whyPhoto)"/>
</svg>
<div class="feature" style="left:167px;top:3032px">
  <svg width="56" height="56" viewBox="0 0 56 56" fill="none" stroke="#222" stroke-width="2"><circle cx="28" cy="30" r="12"/><circle cx="28" cy="30" r="6"/><path d="M20 40l-4 14 12-6 12 6-4-14M8 14l3 3M48 14l-3 3M28 4v5"/></svg>
  <h3>EXPERIENCED</h3><p>Lorem ipsum dolor sit amet, consetetur sadipscing elitr.</p>
</div>
<div class="feature" style="left:754px;top:3021px">
  <svg width="60" height="56" viewBox="0 0 60 56" fill="none" stroke="#222" stroke-width="2"><path d="M4 28L30 6l26 22M10 23v29h40V23"/><path d="M22 34l8-6 8 6v12H22z"/></svg>
  <h3>INSURED</h3><p>Lorem ipsum dolor sit amet, consetetur sadipscing elitr.</p>
</div>
<div class="feature" style="left:236px;top:3216px">
  <svg width="58" height="56" viewBox="0 0 58 56" fill="none" stroke="#222" stroke-width="2"><path d="M29 4l14 5v10c0 8-6 13-14 16-8-3-14-8-14-16V9z"/><path d="M23 19l4 4 8-8M4 36l10-4 10 8 8-2 6 6-10 8-14-4-10 2M54 36l-10-4"/></svg>
  <h3>TRUSTED</h3><p>Lorem ipsum dolor sit amet, consetetur sadipscing elitr.</p>
</div>
<div class="feature" style="left:782px;top:3209px">
  <svg width="56" height="56" viewBox="0 0 56 56" fill="none" stroke="#222" stroke-width="2"><circle cx="28" cy="28" r="24"/><circle cx="28" cy="28" r="17"/><path d="M20 28l6 6 11-12"/></svg>
  <h3>WARRANTY</h3><p>Lorem ipsum dolor sit amet, consetetur sadipscing elitr.</p>
</div>

<!-- Owner promise -->
<section class="promise" role="img" aria-label="Dim photo of an unfinished interior room">
  <blockquote>You deserve timely service, high quality materials, expert installation,<br>&nbsp;and an Stoneward warranty. That is what we promise to deliver.<br>&nbsp;I invite you to put us to the test today</blockquote>
  <span class="rule"></span>
  <p class="owner">DALE HARMON</p>
  <p class="role">Owner</p>
</section>

<!-- Testimonials -->
<h2 class="section-title" style="left:0;right:0;top:3827px;text-align:center">WHAT CLIENT <span>SAYS</span></h2>
<article class="review" style="left:147px"><span class="avatar" role="img" aria-label="Client photo"></span><p class="who">MARCUS T.</p><p class="stars">★★★★★</p><p>I never dreamed my roof would look this good. I thought I had to replace it. Thank you Stoneward for saving me thousands of dollars.</p></article>
<article class="review" style="left:457px"><span class="avatar" role="img" aria-label="Client photo"></span><p class="who">MARCUS T.</p><p class="stars">★★★★★</p><p>I never dreamed my roof would look this good. I thought I had to replace it. Thank you Stoneward for saving me thousands of dollars.</p></article>
<article class="review" style="left:766px"><span class="avatar" role="img" aria-label="Client photo"></span><p class="who">MARCUS T.</p><p class="stars">★★★★★</p><p>I never dreamed my roof would look this good. I thought I had to replace it. Thank you Stoneward for saving me thousands of dollars.</p></article>
<div class="dots" style="left:558px;top:4207px"><span></span><span class="on"></span><span></span></div>

<!-- Footer -->
<footer class="site-footer">
  <div class="footer-brand"><span class="brand-mark"></span><span class="brand-name">STONEWARD</span></div>
  <p class="footer-tag">Stoneward Construction is your source for<br>roofing and siding in Minnesota.</p>
  <p class="footer-links">Abou Us | Conctact | Career | FInancing | Blog</p>
  <div class="footer-contact">
    <span><svg width="24" height="24" viewBox="0 0 24 24"><path fill="#bfbfbf" d="M6.6 10.8a15 15 0 006.6 6.6l2.2-2.2c.3-.3.7-.4 1-.2 1.1.4 2.3.6 3.6.6.6 0 1 .4 1 1V20c0 .6-.4 1-1 1A17 17 0 013 4c0-.6.4-1 1-1h3.5c.6 0 1 .4 1 1 0 1.3.2 2.5.6 3.6.1.3 0 .7-.2 1z"/></svg>(+1) 555 014 2290</span>
    <span><svg width="24" height="20" viewBox="0 0 24 20"><path fill="#bfbfbf" d="M2 6l10 6 10-6v12H2z"/><path fill="#bfbfbf" d="M2 4l10 6 10-6V2H2z"/></svg>hello@stonewardbuild.example</span>
    <span><svg width="20" height="26" viewBox="0 0 20 26"><path fill="#bfbfbf" d="M10 0a10 10 0 00-10 10c0 7 10 16 10 16s10-9 10-16A10 10 0 0010 0zm0 14a4 4 0 110-8 4 4 0 010 8z"/></svg>418 Cedar Lane, Duluth</span>
  </div>
  <p class="copyright">2024 Stoneward Construction. All rights reserved</p>
</footer>

</body>
</html>
```